Velvor IT Services Business Card

Velvor IT Services are a Perth based IT Services company. We would like to incorporate our company logo (attached) and stick with the blue that is in that design. I would like a clean look design that isn't too busy, yet creates a lasting image that is instantly recognisable in the recipients mind.

Target Market(s)

The target audience is small/medium business owners.

Industry/Entity Type

Business

Font styles to use
Serif
Sans Serif

Colors

Designer to choose colors to be used in the design.

Requirements
Must have
• The design should include:
Business name: Velvor IT Services
Directors Name: Marcus Dredge
Phone Number: 0483 906 452
Email: support@velvorit.com.au
Website: www.velvorit.com.au

```html
<!DOCTYPE html>
<html lang="en">
<head>
<meta charset="utf-8">
<title>Velvor IT Services Business Card</title>
<link href="https://fonts.googleapis.com/css2?family=Arimo:wght@400;700&display=swap" rel="stylesheet">
<style>
  :root {
    --page-bg: #e9eaec;
    --brand-blue: #1a4fae;
    --brand-deep: #0a2570;
    --brand-light: #2b67cc;
    --rule-blue: #8aa3d6;
    --ink: #222428;
    --card-white: #ffffff;
  }
  * { margin: 0; padding: 0; box-sizing: border-box; }
  html, body {
    width: 1200px;
    height: 873px;
    overflow: hidden;
    background: var(--page-bg);
    font-family: "Arimo", Arial, sans-serif;
  }
  .sheet {
    width: 1200px;
    height: 873px;
    display: flex;
    align-items: center;
    justify-content: center;
    gap: 60px;
  }
  .card {
    position: relative;
    width: 520px;
    height: 296px;
    overflow: hidden;
    box-shadow: 0 6px 18px rgba(0, 0, 0, 0.18);
  }

  /* Front: blue face */
  .card--front {
    background: radial-gradient(ellipse at 50% 50%, var(--brand-light) 0%, var(--brand-blue) 45%, var(--brand-deep) 100%);
    display: flex;
    align-items: center;
    justify-content: center;
  }
  .brand {
    display: flex;
    align-items: center;
    gap: 12px;
  }
  .brand__mark {
    width: 22px;
    height: 22px;
  }
  .brand__name {
    font-weight: 400;
    letter-spacing: 0.5px;
  }
  .card--front .brand__mark { background: var(--card-white); }
  .card--front .brand__name { color: var(--card-white); font-size: 26px; }

  /* Back: white face */
  .card--back { background: var(--card-white); }
  .card--back .brand {
    position: absolute;
    left: 34px;
    top: 50px;
  }
  .card--back .brand__mark { background: var(--brand-blue); width: 20px; height: 20px; }
  .card--back .brand__name { color: var(--brand-blue); font-size: 21px; }

  .holder {
    position: absolute;
    right: 86px;
    top: 128px;
    text-align: right;
  }
  .holder__name {
    color: var(--brand-blue);
    font-size: 15px;
    line-height: 1.1;
  }
  .holder__role {
    color: var(--ink);
    font-size: 11px;
    margin-top: 3px;
  }
  .divider {
    position: absolute;
    left: 34px;
    right: 68px;
    top: 148px;
    height: 1px;
    background: var(--rule-blue);
  }

  .contacts {
    position: absolute;
    left: 34px;
    bottom: 40px;
    list-style: none;
    font-size: 12px;
    color: var(--ink);
  }
  .contacts li {
    display: flex;
    align-items: center;
    gap: 8px;
    line-height: 18px;
  }
  .contacts svg {
    width: 11px;
    height: 11px;
    fill: var(--brand-blue);
    flex: none;
  }

  .accent-cluster {
    position: absolute;
    right: 0;
    bottom: 0;
    width: 96px;
    height: 118px;
    background: linear-gradient(135deg, rgba(26, 79, 174, 0) 0%, rgba(26, 79, 174, 0.55) 55%, var(--brand-blue) 100%);
  }
</style>
</head>
<body>
  <main class="sheet">
    <section class="card card--front" aria-label="Business card front">
      <div class="brand">
        <span class="brand__mark"></span>
        <span class="brand__name">Velvor IT Services</span>
      </div>
    </section>

    <section class="card card--back" aria-label="Business card back">
      <div class="brand">
        <span class="brand__mark"></span>
        <span class="brand__name">Velvor IT Services</span>
      </div>

      <div class="holder">
        <p class="holder__name">Marcus Dredge</p>
        <p class="holder__role">Director</p>
      </div>
      <div class="divider"></div>

      <ul class="contacts">
        <li>
          <svg viewBox="0 0 24 24" aria-hidden="true"><path d="M6.6 10.8c1.4 2.8 3.8 5.1 6.6 6.6l2.2-2.2c.3-.3.7-.4 1-.2 1.1.4 2.3.6 3.6.6.6 0 1 .4 1 1V20c0 .6-.4 1-1 1C10.6 21 3 13.4 3 4c0-.6.4-1 1-1h3.5c.6 0 1 .4 1 1 0 1.3.2 2.5.6 3.6.1.3 0 .7-.2 1l-2.3 2.2z"/></svg>
          <span>0483 906 452</span>
        </li>
        <li>
          <svg viewBox="0 0 24 24" aria-hidden="true"><path d="M2 5h20v14H2V5zm2 2v.5l8 5 8-5V7H4zm0 2.8V17h16V9.8l-8 5-8-5z"/></svg>
          <span>support@velvorit.com.au</span>
        </li>
        <li>
          <svg viewBox="0 0 24 24" aria-hidden="true"><path d="M12 2a10 10 0 1 0 0 20 10 10 0 0 0 0-20zm6.9 6h-3a15 15 0 0 0-1.3-3.9A8 8 0 0 1 18.9 8zM12 4c.8 1.2 1.5 2.5 1.9 4h-3.8c.4-1.5 1.1-2.8 1.9-4zM4.3 14a8 8 0 0 1 0-4h3.4a16 16 0 0 0 0 4H4.3zm.8 2h3a15 15 0 0 0 1.3 3.9A8 8 0 0 1 5.1 16zm3-8h-3a8 8 0 0 1 4.3-3.9C8.9 5.3 8.4 6.6 8.1 8zM12 20c-.8-1.2-1.5-2.5-1.9-4h3.8c-.4 1.5-1.1 2.8-1.9 4zm2.3-6H9.7a14 14 0 0 1 0-4h4.6a14 14 0 0 1 0 4zm.3 5.9c.6-1.2 1-2.5 1.3-3.9h3a8 8 0 0 1-4.3 3.9zm1.7-5.9a16 16 0 0 0 0-4h3.4a8 8 0 0 1 0 4h-3.4z"/></svg>
          <span>www.velvorit.com.au</span>
        </li>
      </ul>

      <div class="accent-cluster" role="img" aria-label="Decorative cluster of small blue squares"></div>
    </section>
  </main>
</body>
</html>
```